Note/Card sent to show appreciation to partners who worked with us to improve local communities

I'd like a simple note/card designed for a wide audience. Originally, I called this a "Thanksgiving Card," but it's really just a card to be sent around Thanksgiving, not specifically celebrating the Thanksgiving holiday. We plan to send the card out just prior to Thanksgiving 2017 (Nov. 24, 2017). I work at a regulated electric utility, and we'd like to say thank you to the many stakeholders who we partner with throughout the year to support initiatives that help to improve our state and create opportunities for economic growth. I'm interested mostly in the design of the card, not the simple verbiage on the inside.
Customers, charitable foundations, nonprofits, advocacy groups, industry associations, friends

```html
<!DOCTYPE html>
<html lang="en">
<head>
<meta charset="utf-8">
<title>Happy Thanksgiving – Customer Note</title>
<link rel="stylesheet" href="https://fonts.googleapis.com/css2?family=Libre+Baskerville:wght@400;700&family=Old+Standard+TT:wght@400&display=swap">
<style>
  :root {
    --paper: #ffffff;
    --ink: #6b6b6b;
    --frame: #727272;
    --placeholder-cool: #e3e8ef;
    --placeholder-green: #a9c2b0;
  }
  html, body {
    margin: 0;
    padding: 0;
    width: 1200px;
    height: 1200px;
    overflow: hidden;
    background: var(--paper);
  }
  .card {
    position: relative;
    width: 1200px;
    height: 1200px;
    background: var(--paper);
  }
  .card__frame {
    position: absolute;
    left: 44px;
    top: 44px;
    width: 1102px;
    height: 1102px;
    border: 5px solid var(--frame);
  }
  .art__placeholder {
    position: absolute;
  }
  .art__placeholder--bulb {
    left: 432px;
    top: 130px;
    width: 130px;
    height: 222px;
    background: var(--placeholder-cool);
  }
  .art__placeholder--pumpkin {
    left: 612px;
    top: 188px;
    width: 218px;
    height: 174px;
    background: var(--placeholder-green);
  }
  .art__shelf {
    position: absolute;
    left: 387px;
    top: 363px;
    width: 434px;
    height: 11px;
    background: var(--frame);
  }
  .card__title {
    position: absolute;
    left: 0;
    top: 480px;
    width: 1200px;
    height: 90px;
  }
  .card__title text {
    font-family: "Libre Baskerville", serif;
    font-weight: 400;
    font-size: 76px;
    fill: var(--ink);
  }
  .card__rule {
    position: absolute;
    left: 190px;
    top: 589px;
    width: 828px;
    height: 4px;
    background: var(--frame);
  }
  .card__message {
    position: absolute;
    left: 100px;
    top: 638px;
    width: 1000px;
    margin: 0;
    text-align: center;
    font-family: "Old Standard TT", serif;
    font-size: 39px;
    line-height: 48px;
    letter-spacing: 0.6px;
    color: var(--ink);
  }
  .card__dot {
    position: absolute;
    left: 591px;
    top: 1043px;
    width: 25px;
    height: 25px;
    border-radius: 50%;
    background: var(--frame);
  }
</style>
</head>
<body>
<main class="card">
  <div class="card__frame"></div>

  <div class="art__placeholder art__placeholder--bulb" role="img" aria-label="Illustration of a glowing incandescent light bulb"></div>
  <div class="art__placeholder art__placeholder--pumpkin" role="img" aria-label="Watercolour illustration of a green pumpkin with a curling vine"></div>
  <div class="art__shelf"></div>

  <svg class="card__title" viewBox="0 0 1200 90" width="1200" height="90" role="img" aria-label="Happy Thanksgiving">
    <text x="112" y="73" textLength="976" lengthAdjust="spacingAndGlyphs">HAPPY THANKSGIVING</text>
  </svg>
  <div class="card__rule"></div>

  <p class="card__message">
    Thank you for being our valued customers.<br>
    We are grateful for the pleasure of<br>
    serving you and meeting your<br>
    electric utility needs.<br>
    We wish you a lovely Thanksgiving<br>
    and a joyous holiday season.
  </p>

  <div class="card__dot"></div>
</main>
</body>
</html>
```